Eco-Friendly Wheat Straw Drinking Straw Packaging Design Contest

We are seeking talented designers to create a standout packaging design for our eco-friendly wheat straw drinking straws. Our product is an environmentally conscious alternative to plastic and paper straws. We want a design that not only reflects our brand values of sustainability and health but also stands out on store shelves. Please see attached file for detailed brief and requirements.
Updates

Colors
00AB8E
00BBA5
67D7C9
C6EFE9
E9F9F6
59FF00
82FF00
B8FF75
E3FFCB
F4FFEA
FFF300
FFF600
FEFA6F
FFFEC7
FFFEE8

Requirements
Must have
• Clean, modern, and visually appealing design focusing on eco-friendliness and health. Use of earthy colors like green, beige, or brown. Final design should be in Turkish. Please see the brief file attached for further details.
Nice to have
• Scalable design that can be adapted for various packaging sizes. Incorporate creative illustrations or graphics representing wheat, nature, or sustainability.
Should not have
• Avoid overly complex or cluttered designs. Simplicity and clarity are key. Do not use bright or flashy colors that do not align with the natural and eco-friendly theme of the product. Avoid using English text in the final design. All text should be in Turkish, as the product will be marketed locally.

```html
<!DOCTYPE html>
<html lang="tr">
<head>
<meta charset="utf-8">
<title>Buğday Sapı Pipet Ambalajı</title>
<link rel="stylesheet" href="https://fonts.googleapis.com/css2?family=Oswald:wght@400;500;600;700&display=swap">
<style>
  :root {
    --stripe-light: #bce84b;
    --stripe-base: #abdf3d;
    --forest: #137c30;
    --earth: #6b5148;
    --lime-text: #b9e43e;
    --glass-top: #a9cf46;
    --glass-bottom: #8fb63a;
    --page: #ffffff;
  }
  * { margin: 0; padding: 0; box-sizing: border-box; }
  html, body { width: 1200px; height: 1200px; overflow: hidden; background: var(--page); }
  .canvas { position: relative; width: 1200px; height: 1200px; }
  .pack {
    position: absolute; left: 307px; top: 159px; width: 593px; height: 889px;
    border-radius: 16px; overflow: hidden;
    background: repeating-linear-gradient(90deg, var(--stripe-base) 0 15px, var(--stripe-light) 15px 29px);
    font-family: "Oswald", sans-serif;
  }
  .brand {
    position: absolute; left: 168px; top: 58px; display: flex; align-items: center; gap: 12px;
  }
  .brand-dot { width: 80px; height: 80px; border-radius: 50%; border: 6px solid var(--forest); }
  .brand-name { font-size: 52px; font-weight: 600; color: var(--forest); letter-spacing: 1px; line-height: 1; }
  .headline { position: absolute; left: 0; top: 0; width: 593px; height: 520px; z-index: 2; }
  .hill { position: absolute; left: 0; top: 0; width: 593px; height: 889px; }
  .scene {
    position: absolute; left: 262px; top: 560px; width: 331px; height: 329px;
    border-radius: 120px 0 0 0;
    background: linear-gradient(160deg, var(--glass-top), var(--glass-bottom));
  }
  .count { position: absolute; left: 40px; top: 666px; color: var(--lime-text); font-weight: 600; line-height: 1; }
  .count-num { font-size: 80px; }
  .count-unit { font-size: 38px; margin-left: 6px; }
  .features { position: absolute; left: 24px; top: 753px; list-style: none; color: var(--lime-text); font-size: 24px; font-weight: 400; }
  .features li { height: 30px; line-height: 30px; }
  .features li::before { content: "·"; margin-right: 8px; }
</style>
</head>
<body>
<div class="canvas">
  <div class="pack">
    <div class="brand">
      <span class="brand-dot"></span>
      <span class="brand-name">VERDA</span>
    </div>

    <svg class="hill" viewBox="0 0 593 889" aria-hidden="true">
      <path d="M0 501 C150 495 290 560 350 700 L370 889 L0 889 Z" fill="var(--forest)"/>
    </svg>

    <div class="scene" role="img" aria-label="Buğday sapı pipetli limonlu içecek bardağı illüstrasyonu"></div>

    <svg class="headline" viewBox="0 0 593 520" aria-label="Doğal buğday sapından pipet">
      <text x="241" y="230" textLength="268" lengthAdjust="spacingAndGlyphs" font-family="Oswald, sans-serif" font-weight="600" font-size="35" fill="var(--earth)">DOĞAL BUĞDAY SAPINDAN</text>
      <text x="95" y="434" textLength="409" lengthAdjust="spacingAndGlyphs" font-family="Oswald, sans-serif" font-weight="700" font-size="240" fill="var(--forest)">PİPET</text>
      <text x="134" y="475" textLength="326" lengthAdjust="spacingAndGlyphs" font-family="Oswald, sans-serif" font-weight="400" font-size="24" fill="var(--earth)">Topraktan Masaya,Masadan Toprağa!</text>
    </svg>

    <div class="count"><span class="count-num">500</span><span class="count-unit">adet</span></div>
    <ul class="features">
      <li>Doğada çözünür.</li>
      <li>Kimyasal içermez.</li>
      <li>Gıda ile temasa uygundur.</li>
      <li>Tek kullanımlıktır.</li>
    </ul>
  </div>
</div>
</body>
</html>
```